ROLVEN CHICKEN delivery menu

NEED A TAKEAWAY MENU FOR A FAST FOOD TAKEAWAY WITH PICTURES
THE BUSINESS IS CALLED ROLVEN CHICKEN
COLOURS LIKED ARE BLUE RED BLACK AND GREEN. THIS LEAFLET NEEDS TO BE A3 FOLDED AND AIMED AT DELIVERY

Target Market(s)

consumers of fried chicken, pizza etc

Industry/Entity Type

Business

Font styles to use
Serif
Sans Serif

Colors
ec1f27
0355a3
9ccb3b

Requirements
Must have
• pictures of fried chicken, burgers, pizza and kebabs and any other that will fit
Nice to have
• like a Marbrook grilled hen menu

```html
<!DOCTYPE html>
<html lang="en">
<head>
<meta charset="utf-8">
<title>ROLVEN CHICKEN – Side Orders &amp; Meal Deals</title>
<link href="https://fonts.googleapis.com/css2?family=Tinos:ital,wght@0,400;0,700;1,400;1,700&display=swap" rel="stylesheet">
<style>
  :root{
    --red:#be1e2d;
    --ink:#222;
    --veg:#2f8a3c;
    --panel:#e9e9e9;
    --sheet:#ffffff;
    --frame:#2e2e2e;
    --white:#fff;
  }
  *{margin:0;padding:0;box-sizing:border-box}
  html,body{width:848px;height:1200px;overflow:hidden;background:var(--frame)}
  .canvas{width:848px;height:1200px;overflow:hidden;position:relative}
  .menu{position:absolute;left:0;top:0;width:919px;height:1300px;transform:scale(.9227);transform-origin:0 0;
        background:var(--frame);font-family:"Tinos","Times New Roman",serif;color:var(--ink)}
  .abs{position:absolute}

  .hero{left:0;top:0;width:455px;height:335px;background:linear-gradient(180deg,#1c1c1c 0%,#3d3d3d 45%,#5a4a3c 75%,#3a2e25 100%)}
  .hero-band{left:0;top:60px;width:455px;height:175px;background:linear-gradient(90deg,#151515,#2a2a2a 70%,#3a3a3a)}
  .hero-title{left:62px;top:86px;color:var(--white);font-weight:700;font-style:italic;font-size:62px;line-height:58px;letter-spacing:1px}
  .hero-photo{left:12px;top:200px;width:443px;height:135px;border-radius:40px 0 0 0;
              background:radial-gradient(ellipse at 30% 60%,#e8d8b8 0%,#c99a5b 35%,#6d8a3f 60%,#4a3a2a 100%)}
  .size-bar{left:237px;top:275px;width:218px;height:53px;background:var(--red);color:var(--white);
            font-weight:700;font-style:italic;font-size:24px}
  .size-bar span{position:absolute;top:12px}
  .sheet{left:0;width:455px;background:var(--sheet)}
  .price-list{list-style:none;font-style:italic;font-size:15.5px}
  .price-list li{position:absolute;left:15px;height:23px;line-height:23px;white-space:nowrap;z-index:2}
  .price-list .veg{color:var(--veg)}
  .price-list .sm,.price-list .lg{position:absolute;font-weight:700;color:var(--ink)}
  .section-band{left:0;width:455px;height:53px;background:var(--red);color:var(--white);
                font-weight:700;font-style:italic;font-size:24px;padding:13px 0 0 30px}
  .garlic-photo{left:278px;top:826px;width:86px;height:50px;border-radius:20px;
                background:linear-gradient(135deg,#e0b873,#b7822f)}
  .dessert-photo{left:100px;top:1160px;width:260px;height:140px;border-radius:50% 50% 10px 10px;
                 background:radial-gradient(ellipse at 45% 45%,#fbf6ee 0%,#efe3d1 45%,#c2262e 70%,#f3eee6 100%)}

  .card{position:absolute;background:var(--panel)}
  .card-head{position:absolute;left:0;top:0;right:0;background:var(--red);color:var(--white);
             font-weight:700;font-style:italic;font-size:19px;line-height:19px;padding:0 8px 4px 8px;
             display:flex;justify-content:space-between;align-items:flex-end}
  .card-body{position:absolute;left:10px;font-style:italic;font-size:15.5px;line-height:19.5px;z-index:2;white-space:nowrap}
  .card-body .or{color:var(--red)}
  .card-body .veg{color:var(--veg)}
  .meal-photo{position:absolute;z-index:1;border-radius:12px;
              background:radial-gradient(ellipse at 60% 60%,#e8a43c 0%,#b85a1e 45%,#c0232c 75%,rgba(233,233,233,0) 100%)}
</style>
</head>
<body>
<div class="canvas">
<main class="menu">

  <div class="abs hero"></div>
  <div class="abs hero-band"></div>
  <h1 class="abs hero-title">SIDE<br>ORDERS</h1>
  <div class="abs hero-photo" role="img" aria-label="Photo of kebab plates with salad and wraps on a wooden table"></div>
  <div class="abs size-bar"><span style="left:18px">SMALL</span><span style="left:132px">LARGE</span></div>

  <div class="abs sheet" style="top:335px;height:422px"></div>
  <ul class="price-list">
    <li style="top:338px">Chips (French Fries) <span class="veg">(V)</span><span class="sm" style="left:255px">£1.70</span><span class="lg" style="left:363px">£2.30</span></li>
    <li style="top:361px">Cheesy Chips <span class="veg">(V)</span><span class="sm" style="left:255px">£3.00</span><span class="lg" style="left:363px">£3.50</span></li>
    <li style="top:384px">Onion Rings <span class="veg">(V)</span><span class="lg" style="left:363px">£3.00</span></li>
    <li style="top:407px">Garlic Mushrooms <span class="veg">(V)</span><span class="lg" style="left:363px">£3.00</span></li>
    <li style="top:430px">Mozzarella Stick <span class="veg">(V)</span><span class="lg" style="left:363px">£3.00</span></li>
    <li style="top:453px">Potato Wedges + Dip <span class="veg">(V)</span><span class="lg" style="left:363px">£2.50</span></li>
    <li style="top:476px">BBQ Beans <span class="veg">(V)</span><span class="lg" style="left:363px">£1.50</span></li>
    <li style="top:499px">Coleslaw <span class="veg">(V)</span><span class="lg" style="left:363px">£1.50</span></li>
    <li style="top:522px">Curry Sauce <span class="veg">(V)</span><span class="lg" style="left:363px">£1.50</span></li>
    <li style="top:545px">Spicy Chicken Bites<span class="lg" style="left:363px">£3.50</span></li>
    <li style="top:568px">Chicken Dippers (6 Pcs)<span class="lg" style="left:363px">£3.50</span></li>
    <li style="top:591px">BBQ Chicken Wings (6 Pcs)<span class="lg" style="left:363px">£3.50</span></li>
    <li style="top:614px">Rice <span class="veg">(V)</span><span class="lg" style="left:363px">£2.50</span></li>
    <li style="top:637px">Hummus in Pitta with Salad <span class="veg">(V)</span><span class="lg" style="left:363px">£3.00</span></li>
    <li style="top:660px">Chips in Pitta <span class="veg">(V)</span><span class="lg" style="left:363px">£3.00</span></li>
    <li style="top:683px">Hummus in a Tub <span class="veg">(V)</span><span class="lg" style="left:363px">£1.50</span></li>
    <li style="top:706px">Tzatziki <span class="veg">(V)</span><span class="lg" style="left:363px">£1.50</span></li>
    <li style="top:729px">Halloumi Stick <span class="veg">(V)</span><span class="lg" style="left:363px">£3.50</span></li>
  </ul>

  <h2 class="abs section-band" style="top:765px">GARLIC BREADS</h2>
  <div class="abs sheet" style="top:818px;height:152px"></div>
  <div class="abs garlic-photo" role="img" aria-label="Photo of two garlic bread torpedoes"></div>
  <ul class="price-list">
    <li style="top:826px">C Torpedo<span class="lg" style="left:363px">£2.50</span></li>
    <li style="top:849px">Torpedo with Cheese<span class="lg" style="left:363px">£3.00</span></li>
    <li style="top:872px">Torpedo with Cheese and Mushroom<span class="lg" style="left:363px">£3.50</span></li>
    <li style="top:895px">Torpedo with Cheese and Pepperoni<span class="lg" style="left:363px">£3.80</span></li>
    <li style="top:918px">Torpedo with Cheese and Jalapeno<span class="lg" style="left:363px">£3.50</span></li>
    <li style="top:941px">Torpedo with Cheese and Bacon<span class="lg" style="left:363px">£3.50</span></li>
  </ul>

  <h2 class="abs section-band" style="top:978px">DESSERTS</h2>
  <div class="abs sheet" style="top:1032px;height:268px"></div>
  <ul class="price-list">
    <li style="top:1041px">White Chocolate Raspberry Cheese Cake<span class="lg" style="left:363px">£3.00</span></li>
    <li style="top:1064px">Chocolate Cheese Cake<span class="lg" style="left:363px">£2.50</span></li>
    <li style="top:1087px">Strawberry Cheese Cake<span class="lg" style="left:363px">£2.50</span></li>
    <li style="top:1110px">Eton mess Cheese Cake<span class="lg" style="left:363px">£3.00</span></li>
    <li style="top:1133px">Chocolate Fudge Lumpy Bumpy<span class="lg" style="left:363px">£3.50</span></li>
  </ul>
  <div class="abs dessert-photo" role="img" aria-label="Photo of a slice of strawberry cheesecake with sauce"></div>

  <!-- Meal deals: column A -->
  <section class="card" style="left:458px;top:0;width:230px;height:190px">
    <h3 class="card-head" style="height:55px"><span>CHICKEN<br>DINNER MEAL</span><span>£5.00</span></h3>
    <p class="card-body" style="top:57px">2 Pcs of Chicken<br>Regular Fries<br>Beans or Coleslaw<br>or Can of Soft Drink</p>
    <div class="meal-photo" style="left:128px;top:137px;width:100px;height:51px" role="img" aria-label="Photo of fried chicken, fries and a drink can"></div>
  </section>

  <section class="card" style="left:458px;top:193px;width:230px;height:157px">
    <h3 class="card-head" style="height:47px"><span>¼ POUNDER<br>MEAL</span><span>£5.50</span></h3>
    <p class="card-body" style="top:50px">¼ Pounder Burger<br>Regular Fries<br>Can of Soft Drink<br><span class="veg">(V)</span></p>
    <div class="meal-photo" style="left:142px;top:56px;width:86px;height:98px" role="img" aria-label="Photo of a burger, fries and a drink can"></div>
  </section>

  <section class="card" style="left:458px;top:357px;width:230px;height:160px">
    <h3 class="card-head" style="height:33px"><span>FULL HOUSE</span><span>£6.00</span></h3>
    <p class="card-body" style="top:42px">Portion of Ribs<br>1 Piece of Chicken<br>Regular Fries<br>Can of Soft Drink</p>
    <div class="meal-photo" style="left:146px;top:48px;width:82px;height:110px" role="img" aria-label="Photo of ribs, fried chicken, fries and a drink can"></div>
  </section>

  <section class="card" style="left:458px;top:520px;width:230px;height:163px">
    <h3 class="card-head" style="height:47px"><span>CHICKEN<br>WRAP MEAL</span><span>£5.50</span></h3>
    <p class="card-body" style="top:55px">Chicken Fillet Wrap<br>Regular Fries<br>Can of Soft Drink</p>
    <div class="meal-photo" style="left:100px;top:116px;width:128px;height:45px" role="img" aria-label="Photo of a chicken wrap, fries and a drink can"></div>
  </section>

  <section class="card" style="left:458px;top:686px;width:230px;height:162px">
    <h3 class="card-head" style="height:44px"><span>FAMILY MEAL</span><span>£17.00</span></h3>
    <p class="card-body" style="top:50px">12 Pcs Chicken<br>4 Fries, Colesla Beans,<br>Corn on the Cob<br>1.5 Litre Bottle<br>Drink</p>
    <div class="meal-photo" style="left:140px;top:92px;width:88px;height:68px" role="img" aria-label="Photo of a family bucket of fried chicken with sides and a bottle drink"></div>
  </section>

  <section class="card" style="left:458px;top:851px;width:230px;height:221px">
    <h3 class="card-head" style="height:44px"><span>PIZZA DEAL 2</span><span>£16.00</span></h3>
    <p class="card-body" style="top:54px">2 x 10” Any Pizza<br>2 x Garlic Torpedo<br>with Cheese<br><span style="display:block;height:12px"></span>Onion Rings<br>1.5 Litre Bottle Drink</p>
    <div class="meal-photo" style="left:150px;top:58px;width:78px;height:84px" role="img" aria-label="Photo of pizza, onion rings and a bottle drink"></div>
  </section>

  <section class="card" style="left:458px;top:1075px;width:230px;height:225px">
    <h3 class="card-head" style="height:50px"><span>BONELESS<br>CHICKEN DEAL</span><span>£19.00</span></h3>
    <p class="card-body" style="top:53px">6 Chicken Fillets<br>10 Nuggets<br>Portion Spicy Chicken Bites<br>Portion Popcorn Chicken<br>4 Small Chips<br>1.5 Litre Bottle<br>Drink</p>
    <div class="meal-photo" style="left:118px;top:134px;width:110px;height:89px" role="img" aria-label="Photo of chicken fillets, nuggets, chips and a bottle drink"></div>
  </section>

  <!-- Meal deals: column B -->
  <section class="card" style="left:690px;top:0;width:229px;height:190px">
    <h3 class="card-head" style="height:55px"><span>FILLET<br>BURGER MEAL</span><span>£5.00</span></h3>
    <p class="card-body" style="top:57px">Chicken Fillet Burger<br>Regular Fries<br>Can of Soft Drink</p>
    <div class="meal-photo" style="left:115px;top:118px;width:112px;height:70px" role="img" aria-label="Photo of a chicken fillet burger, fries and a drink can"></div>
  </section>

  <section class="card" style="left:690px;top:193px;width:229px;height:160px">
    <h3 class="card-head" style="height:47px"><span>BBQ SPARE<br>RIBS MEAL</span><span>£5.50</span></h3>
    <p class="card-body" style="top:50px">Portion of Ribs<br>Regular Fries<br>Can of Soft Drink</p>
    <div class="meal-photo" style="left:140px;top:54px;width:87px;height:103px" role="img" aria-label="Photo of BBQ ribs, fries and a drink can"></div>
  </section>

  <section class="card" style="left:690px;top:357px;width:229px;height:160px">
    <h3 class="card-head" style="height:48px"><span>CHICKEN<br>VARIETY MEAL</span><span>£5.50</span></h3>
    <p class="card-body" style="top:50px">2 Pcs of chicken<br>2 Hot Wings<br>Regular Fries<br>Can of Soft<br>Drink</p>
    <div class="meal-photo" style="left:132px;top:55px;width:95px;height:103px" role="img" aria-label="Photo of fried chicken, hot wings, fries and a drink can"></div>
  </section>

  <section class="card" style="left:690px;top:520px;width:229px;height:163px">
    <h3 class="card-head" style="height:47px"><span>DONER<br>WRAP MEAL</span><span>£5.50</span></h3>
    <p class="card-body" style="top:51px">Lamb Doner Wrap<br>Regular Fries<br>Can of Soft Drink</p>
    <div class="meal-photo" style="left:100px;top:112px;width:127px;height:49px" role="img" aria-label="Photo of a doner wrap, fries and a drink can"></div>
  </section>

  <section class="card" style="left:690px;top:686px;width:229px;height:206px">
    <h3 class="card-head" style="height:46px"><span>PIZZA DEAL 1</span><span>£23.00</span></h3>
    <p class="card-body" style="top:50px">2 x 12” Any Pizza<br>2 x Garlic Torpedo<br>with Cheese<br><span style="display:block;height:12px"></span>10 Nuggets Garlic<br>Mushrooms<br>1.5 Litre Bottle<br>Drink</p>
    <div class="meal-photo" style="left:150px;top:55px;width:77px;height:120px" role="img" aria-label="Photo of pizza, nuggets and a bottle drink"></div>
  </section>

  <section class="card" style="left:690px;top:895px;width:229px;height:218px">
    <h3 class="card-head" style="height:45px"><span>KEBAB DEAL</span><span>£14.00</span></h3>
    <p class="card-body" style="top:50px">2 x Large Doners<br>2 Chips<br>Onion Rings<br>2 Can of Soft<br>Drink</p>
    <div class="meal-photo" style="left:136px;top:70px;width:91px;height:145px" role="img" aria-label="Photo of doner kebabs, chips, onion rings and drink cans"></div>
  </section>

  <section class="card" style="left:690px;top:1116px;width:229px;height:184px">
    <h3 class="card-head" style="height:31px"><span>KIDS MEAL</span><span>£3.40</span></h3>
    <p class="card-body" style="top:32px">Popcorn Chicken<br>with Chips and<br>Can of Drink <span class="or">or</span><br>4 Chicken<br>Nuggets with<br>Chips and Can of<br>Drink</p>
    <div class="meal-photo" style="left:146px;top:35px;width:81px;height:147px" role="img" aria-label="Photo of popcorn chicken, chips, corn and a drink can"></div>
  </section>

</main>
</div>
</body>
</html>
```